Gordon the Glazier
stationary
Gordon the Glazier -
Creative Brief
Simple
Desmond Pryce
PO Box 417 KELDARRA VIC 3062
gordon@gordontheglazier.com.au
www.gordontheglazier.com.au
I don't need my name or address on the business card -- it just needs to be a general "Gordon the Glazier" card with phone and email contact and web address. Could you also put "Member of the TGWB" somewhere -- this text doesn't have to be bold/eye-catching. It would be good if you could design a business card, letterhead and envelope design

```html
<!DOCTYPE html>
<html lang="en">
<head>
<meta charset="utf-8">
<title>Gordon the Glazier — Stationery</title>
<link href="https://fonts.googleapis.com/css2?family=Montserrat:wght@500;700&family=Open+Sans:wght@400;600&display=swap" rel="stylesheet">
<style>
  :root{
    --navy:#2b3a8c;
    --navy-dark:#1f2b6e;
    --sky:#1c9ad6;
    --paper:#ffffff;
    --ghost:#e6ebf2;
    --backdrop:#e9e7e3;
    --ink:#3b4257;
  }
  *{box-sizing:border-box;margin:0;padding:0}
  html,body{width:1200px;height:701px;overflow:hidden;background:var(--backdrop)}
  body{position:relative;font-family:"Open Sans",Arial,sans-serif;color:var(--ink)}
  .sheet{position:absolute;background:var(--paper);box-shadow:0 2px 8px rgba(0,0,0,.18);overflow:hidden}

  .brand{display:flex;align-items:center;gap:8px}
  .brand-mark{width:22px;height:22px;background:var(--navy);flex:none}
  .brand-name{font-family:"Montserrat",Arial,sans-serif;font-weight:700;color:var(--navy);font-size:17px;line-height:1.1}

  .ghost-square{position:absolute;background:var(--ghost)}

  /* envelope back */
  .envelope-back{left:70px;top:60px;width:380px;height:190px}
  .envelope-back svg{position:absolute;inset:0}
  .flap-name{position:absolute;left:0;right:0;top:108px;text-align:center;font-family:"Montserrat",Arial,sans-serif;font-weight:700;font-size:11px;color:var(--paper)}

  /* envelope front */
  .envelope-front{left:70px;top:290px;width:380px;height:190px}
  .envelope-front .brand{position:absolute;left:22px;top:22px}
  .envelope-front .ghost-square{right:24px;top:58px;width:92px;height:100px}
  .footer-band{position:absolute;left:0;right:0;bottom:0;height:16px;background:var(--navy);color:#dfe5f5;font-size:6.5px;line-height:16px;padding-left:14px;letter-spacing:.2px}
  .footer-rule{position:absolute;left:0;right:0;bottom:16px;height:3px;background:var(--sky)}

  /* letterhead */
  .letterhead{left:500px;top:40px;width:380px;height:537px}
  .letterhead .brand{position:absolute;left:24px;top:24px}
  .letterhead .ghost-square{right:24px;bottom:48px;width:80px;height:92px}

  /* business cards */
  .card{width:270px;height:154px}
  .card-back{left:910px;top:250px;background:var(--navy)}
  .card-back .brand{position:absolute;left:0;right:0;top:52px;justify-content:center}
  .card-back .brand-mark{background:var(--sky);width:18px;height:18px}
  .card-back .brand-name{color:var(--paper);font-size:14px}
  .card-back .card-url{position:absolute;right:16px;top:16px;font-size:7px;color:#cfd8f2}
  .card-front{left:910px;top:430px}
  .card-front svg{position:absolute;inset:0}
  .card-front .brand{position:absolute;left:16px;top:18px}
  .card-front .brand-name{font-size:14px}
  .card-front .brand-mark{width:18px;height:18px}
  .card-details{position:absolute;left:16px;top:62px;font-size:7.5px;line-height:1.55;color:var(--ink)}
  .card-details b{font-weight:600;color:var(--navy)}
  .card-member{position:absolute;left:16px;bottom:14px;font-size:6.5px;color:#7a8196}
</style>
</head>
<body>

<section class="sheet envelope-back" aria-label="Envelope, back">
  <svg width="380" height="190" viewBox="0 0 380 190" aria-hidden="true">
    <polygon points="0,0 380,0 190,70" fill="#f4f6fa"/>
    <polyline points="0,0 190,70 380,0" fill="none" stroke="#c9cfdc" stroke-width="1"/>
    <polygon points="0,190 0,78 190,140 380,78 380,190" fill="var(--navy)"/>
    <polyline points="0,78 190,140 380,78" fill="none" stroke="var(--sky)" stroke-width="3"/>
  </svg>
  <div class="flap-name">Gordon the Glazier</div>
</section>

<section class="sheet envelope-front" aria-label="Envelope, front">
  <div class="brand"><span class="brand-mark"></span><span class="brand-name">Gordon the Glazier</span></div>
  <div class="ghost-square"></div>
  <div class="footer-rule"></div>
  <div class="footer-band">PO Box 417 KELDARRA VIC 3062 &nbsp;|&nbsp; Ph 0400 123 456</div>
</section>

<section class="sheet letterhead" aria-label="Letterhead">
  <div class="brand"><span class="brand-mark"></span><span class="brand-name">Gordon the Glazier</span></div>
  <div class="ghost-square"></div>
  <div class="footer-rule"></div>
  <div class="footer-band">PO Box 417 KELDARRA VIC 3062 &nbsp;|&nbsp; Ph 0400 123 456 &nbsp;|&nbsp; gordon@gordontheglazier.com.au &nbsp;|&nbsp; www.gordontheglazier.com.au</div>
</section>

<section class="sheet card card-back" aria-label="Business card, back">
  <div class="card-url">www.gordontheglazier.com.au</div>
  <div class="brand"><span class="brand-mark"></span><span class="brand-name">Gordon the Glazier</span></div>
</section>

<section class="sheet card card-front" aria-label="Business card, front">
  <svg width="270" height="154" viewBox="0 0 270 154" aria-hidden="true">
    <path d="M170,0 H270 V154 H120 C210,130 230,60 170,0 Z" fill="var(--navy)"/>
    <path d="M165,0 C225,60 205,130 115,154" fill="none" stroke="var(--sky)" stroke-width="4"/>
  </svg>
  <div class="brand"><span class="brand-mark"></span><span class="brand-name">Gordon the Glazier</span></div>
  <div class="card-details">
    <div><b>Phone</b> 0400 123 456</div>
    <div><b>Email</b> gordon@gordontheglazier.com.au</div>
    <div><b>Web</b> www.gordontheglazier.com.au</div>
  </div>
  <div class="card-member">Member of the TGWB</div>
</section>

</body>
</html>
```